Whitcombe Framing Works - Card Design

I am looking to use the logo designs that you already did for me to develop a business card. I would like the card to have a black background and be double sided. I want white and green logo and text. I have attached an inspiration photo of a look that I like. I would like to use the Vertical Logo attached to take up the full front side of the card. On the back where I have my name and information, I would like to have the horizontal logo or maybe even just the image of the 'A' and trees without the text. I am open, but I am looking for something clean and simple and I want the green to really pop! Additional files can be found under Design #: 40593216

Target Market(s)

Homeowners

Industry/Entity Type

Construction

Contact Information for Business Card

Name: Marcus Pellow, Title: Project Manager, Phone: 831.555.0147, Email: whitcombeframingworks@mailbarn.net, address: 418 Juniper Ln, Felton, CA 95092, Lic# 2046318

Colors
00AB8E
00BBA5
67D7C9
C6EFE9
E9F9F6

Requirements
Nice to have
• I would like to see the logos that I have already got from SketchHarbor, though I am open to new ones

```html
<!DOCTYPE html>
<html lang="en">
<head>
<meta charset="utf-8">
<title>Whitcombe Framing Works – Business Card</title>
<link rel="stylesheet" href="https://fonts.googleapis.com/css2?family=Jost:wght@400;500;600&display=swap">
<style>
  :root {
    --backdrop: #939393;
    --card: #242424;
    --card-deep: #1a1a1a;
    --card-soft: #2e2e2e;
    --faint: #303030;
    --green: #3fb54a;
    --white: #ffffff;
    --text-font: "Jost", sans-serif;
  }
  * { margin: 0; padding: 0; box-sizing: border-box; }
  html, body { width: 1200px; height: 1000px; overflow: hidden; }
  body { background: var(--backdrop); font-family: var(--text-font); color: var(--white); position: relative; }

  .card {
    position: absolute; left: 293px; width: 615px; height: 350px;
    border-radius: 28px; background: var(--card); overflow: hidden;
    box-shadow: 0 20px 40px rgba(0, 0, 0, 0.28);
  }
  .card--front { top: 104px; }
  .card--back { top: 504px; }

  /* front */
  .front-texture {
    position: absolute; inset: 0;
    background:
      repeating-linear-gradient(180deg, rgba(0,0,0,0.22) 0 34px, rgba(255,255,255,0.02) 34px 58px),
      linear-gradient(90deg, var(--card-deep) 0%, var(--card) 55%, var(--card-soft) 100%);
  }
  .front-band {
    position: absolute; left: 0; right: 0; top: 128px; height: 96px;
    background: var(--card);
  }
  .front-brand {
    position: absolute; left: 0; right: 0; top: 148px;
    display: flex; align-items: center; justify-content: center; gap: 14px;
  }
  .brand-dot { width: 44px; height: 44px; border-radius: 50%; background: var(--green); flex: none; }
  .front-brand__name { font-size: 38px; font-weight: 600; color: var(--white); letter-spacing: 0.5px; line-height: 56px; }

  /* back */
  .back-decoration { position: absolute; left: 0; top: 0; }
  .back-badge {
    position: absolute; left: 55px; top: 24px; width: 116px; height: 116px;
    border: 3px solid var(--white); border-radius: 50%; background: var(--card-deep);
    display: flex; align-items: center; justify-content: center; text-align: center;
  }
  .back-badge__name { font-size: 15px; font-weight: 600; line-height: 1.15; color: var(--white); }

  .holder { position: absolute; left: 36px; top: 174px; }
  .holder__name { font-size: 18.5px; font-weight: 600; color: var(--green); letter-spacing: 0.8px; text-transform: uppercase; }
  .holder__role { margin-top: 5px; font-size: 11.5px; font-weight: 500; letter-spacing: 2.2px; line-height: 16px; text-transform: uppercase; }

  .divider { position: absolute; left: 37px; top: 252px; width: 521px; height: 2px; background: var(--white); }

  .contact { position: absolute; display: flex; flex-direction: column; gap: 4px; }
  .contact--left { left: 36px; top: 268px; }
  .contact--right { left: 388px; top: 270px; }
  .contact__row { display: flex; align-items: flex-start; gap: 8px; font-size: 14.5px; font-weight: 400; letter-spacing: 0.4px; line-height: 18px; }
  .contact--right .contact__row { font-size: 13.5px; font-weight: 500; text-transform: uppercase; line-height: 20px; }
  .icon { width: 20px; height: 20px; flex: none; }
</style>
</head>
<body>

<section class="card card--front" aria-label="Card front">
  <div class="front-texture" role="img" aria-label="Subtle dark embossed pattern of repeated brand marks"></div>
  <div class="front-band"></div>
  <div class="front-brand">
    <span class="brand-dot"></span>
    <span class="front-brand__name">Whitcombe Framing Works</span>
  </div>
</section>

<section class="card card--back" aria-label="Card back">
  <svg class="back-decoration" width="615" height="350" viewBox="0 0 615 350" aria-hidden="true">
    <circle cx="500" cy="190" r="140" fill="none" stroke="#303030" stroke-width="6"/>
    <text x="345" y="215" font-family="Jost, sans-serif" font-weight="600" font-size="46" fill="#303030">Whitcombe</text>
  </svg>

  <div class="back-badge">
    <span class="back-badge__name">Whitcombe<br>Framing<br>Works</span>
  </div>

  <div class="holder">
    <div class="holder__name">Marcus Pellow</div>
    <div class="holder__role">Project Manager<br>Lic# 2046318</div>
  </div>

  <div class="divider"></div>

  <div class="contact contact--left">
    <div class="contact__row">
      <svg class="icon" viewBox="0 0 20 20" aria-hidden="true"><circle cx="10" cy="10" r="10" fill="#3fb54a"/><path d="M7 5.2l1.6 2.4-1 1.1c.6 1.3 1.5 2.2 2.8 2.8l1.1-1 2.4 1.6-.7 1.6c-3.6.2-7.5-3.7-7.3-7.3z" fill="#242424"/></svg>
      <span>831.555.0147</span>
    </div>
    <div class="contact__row">
      <svg class="icon" viewBox="0 0 20 20" aria-hidden="true"><circle cx="10" cy="10" r="10" fill="#3fb54a"/><rect x="5" y="6.5" width="10" height="7" fill="#242424"/><path d="M5 6.5l5 4 5-4" fill="none" stroke="#3fb54a" stroke-width="1"/></svg>
      <span>whitcombeframingworks@mailbarn.net</span>
    </div>
  </div>

  <div class="contact contact--right">
    <div class="contact__row">
      <svg class="icon" viewBox="0 0 20 20" aria-hidden="true"><circle cx="10" cy="10" r="10" fill="#3fb54a"/><path d="M10 4.5a3.5 3.5 0 0 0-3.5 3.5c0 2.6 3.5 6.5 3.5 6.5s3.5-3.9 3.5-6.5A3.5 3.5 0 0 0 10 4.5z" fill="#242424"/><circle cx="10" cy="8" r="1.3" fill="#3fb54a"/></svg>
      <span>418 Juniper Ln, Felton<br>CA 95092</span>
    </div>
  </div>
</section>

</body>
</html>
```